Aviation: IFR Study Guide Book Cover

We need a book cover (front and back) designed for an Instrument Flight Rules (IFR) study guide used by helicopter and airplane pilots to obtain an instrument rating for a helicopter or airplane. Below is the title and subtitles.

TITLE: IFR STUDY GUIDE
SUBTITLE 1: Checkride Preparation for Airplane and Helicopter Pilots
SUBTITLE 2: Prepare for your Instrument Rating with Confidence

We have also upload recommended text to be included on the back cover. In addition, we included images of similar book covers that we like and ones that we do not like. Below are links to two others books by the author.

https://www.shopvendrix.com/Rotorcraft-Exam-Handbook-oral-flighttest/dp/204715382K
https://www.shopvendrix.com/Manual-Floatcraft-Piloting-Marcus-Holloway/dp/1702538146

Target Market(s)

Flight students

Industry/Entity Type

Aviation

Requirements
Nice to have
• helicopter and airplane

```html
<!DOCTYPE html>
<html lang="en">
<head>
<meta charset="utf-8">
<title>IFR Study Guide – Cover Spread</title>
<link rel="stylesheet" href="https://fonts.googleapis.com/css2?family=Oswald:wght@600;700&family=Montserrat:wght@400;500;600;700&display=swap">
<style>
  :root{
    --paper:#ffffff;
    --ink:#050505;
    --gold:#d4ae4f;
    --red:#db3a26;
    --white:#ffffff;
    --photo-dark:#1b1d22;
    --photo-mid:#3a3f4a;
    --author-grey:#a7adb3;
  }
  html,body{margin:0;padding:0;overflow:hidden;background:var(--paper);}
  .canvas{position:relative;width:1200px;height:1200px;overflow:hidden;background:var(--paper);font-family:"Montserrat",sans-serif;color:var(--white);}
  .spread{position:absolute;left:0;top:216px;width:1200px;height:769px;background:var(--ink);}
  .red-band{position:absolute;left:0;top:682px;width:1200px;height:48px;background:var(--red);}
  .title{font-family:"Oswald",sans-serif;font-weight:700;color:var(--gold);margin:0;line-height:1;letter-spacing:-2px;white-space:nowrap;transform:scaleX(.86);transform-origin:left top;}

  /* back cover */
  .back{position:absolute;left:66px;top:0;width:454px;}
  .back .title{position:absolute;left:53px;top:50px;font-size:66px;}
  .back-tagline{position:absolute;left:0;top:142px;width:454px;text-align:center;font-size:14px;font-weight:400;}
  .back-copy{position:absolute;left:1px;top:173px;width:442px;font-size:11px;line-height:13.7px;text-align:justify;margin:0;}
  .back-copy p{margin:0 0 13.7px;}
  .topics{position:absolute;left:0;top:337px;width:446px;border:1.5px solid var(--gold);border-radius:8px;border-collapse:separate;border-spacing:0;font-size:11px;font-weight:700;overflow:hidden;}
  .topics td{border-right:1.5px solid var(--gold);border-bottom:1.5px solid var(--gold);padding:5px 4px;height:12px;white-space:nowrap;}
  .topics td:last-child{border-right:none;}
  .topics tr:last-child td{border-bottom:none;}
  .back-author{position:absolute;left:0;top:432px;width:454px;text-align:center;font-size:20px;font-weight:500;letter-spacing:1px;}
  .bio{position:absolute;left:0;top:472px;width:453px;font-size:11px;line-height:13.7px;text-align:justify;margin:0;}
  .author-photo{float:left;width:123px;height:114px;margin:1px 5px 0 0;background:var(--author-grey);}
  .code-box{position:absolute;left:434px;top:660px;width:136px;height:82px;border:1px solid #d8d8d8;box-sizing:border-box;}

  /* spine */
  .spine{position:absolute;left:294px;top:57px;width:611px;height:22px;transform:translate(0,0) rotate(-90deg);transform-origin:center;left:293px;top:296px;display:flex;align-items:center;justify-content:space-between;color:var(--gold);white-space:nowrap;}
  .spine-title{font-weight:700;font-size:17px;letter-spacing:1px;}
  .spine-sub{font-size:8.5px;font-weight:400;letter-spacing:.2px;}
  .spine-sub b{font-weight:700;}
  .spine-author{font-size:8.5px;font-weight:700;letter-spacing:.5px;}

  /* front cover */
  .front{position:absolute;left:621px;top:0;width:579px;}
  .front .title{position:absolute;left:58px;top:55px;font-size:90px;}
  .front-sub{position:absolute;left:0;top:181px;width:579px;text-align:center;font-size:21px;line-height:26px;letter-spacing:1px;margin:0;font-weight:400;}
  .front-sub b{font-weight:700;}
  .front-tagline{position:absolute;left:0;top:263px;width:579px;text-align:center;font-size:11px;letter-spacing:.6px;}
  .photo{position:absolute;top:324px;width:205px;height:267px;border:6px solid var(--gold);background:linear-gradient(180deg,var(--photo-mid),var(--photo-dark) 60%,#2a2c33);}
  .photo.airliner{left:67px;}
  .photo.rotorcraft{left:297px;background:linear-gradient(180deg,#7da6cf 0%,#3e4654 22%,var(--photo-dark) 60%,#4a5567);}
  .front-author{position:absolute;left:0;top:681px;width:579px;text-align:center;font-size:35px;font-weight:500;letter-spacing:2px;line-height:48px;}
</style>
</head>
<body>
<div class="canvas">
  <div class="spread">
    <div class="red-band"></div>

    <section class="back">
      <h2 class="title">IFR STUDY GUIDE</h2>
      <div class="back-tagline">Prepare for your IFR check ride with confidence</div>
      <div class="back-copy">
        <p>Becoming an instrument rated pilot is one of the most challenging ratings to obtain. This guide helps prepare you to pass your IFR check ride with confidence. The question-and-answer format is easy to follow and provides detailed explanations for expanded knowledge.</p>
        <p>Includes Helicopter and Airplane Specific Content<br>This guide is designed to prepare an airplane or helicopter pilot the oral portion of the IFR checkride. Unlike other resources, this guide specifically addresses the differences with IFR flight in helicopters. As a dual rated pilot, the author ensures to identify areas of differences between the two categories of IFR flight. The following concepts are addressed within the guide.</p>
      </div>
      <table class="topics">
        <tr><td>• Preflight Actions</td><td>• Enroute Procedures</td><td>• Aeromedical Factors</td></tr>
        <tr><td>• General IFR Concepts</td><td>• Approach Procedures</td><td>• Weather Fundamentals</td></tr>
        <tr><td>• Departure Procedures</td><td>• IFR Emergences</td><td>• Risk Management</td></tr>
      </table>
      <div class="back-author">MARCUS J. HOLLOWAY</div>
      <p class="bio"><span class="author-photo" role="img" aria-label="Author portrait"></span>About the Author: Marcus Holloway is ATP rated pilot and helicopter and fixed-wing instructor. Marcus is the owner and operator Vantage Ridge, LLC which does business as Crestline Aviation and Marlin Aviation. Crestline Aviation provides primary helicopter flight instruction while Marlin Aviation provides seaplane flight instruction and tours. In addition to instructing, Marcus has authored other books to include, The Rotorcraft Exam Handbook, and Manual of Floatcraft Piloting. Marcus lives in Kentucky with his beautiful wife Joanna. They have a daughter, Claire, that is dual rated and employed as a captain for a charter company. Prior to learning to fly, Marcus spent several years in the military as a Special Warfare Combat Craft Crewman in the U.S. Navy and Ranger-qualified infantry officer in the U.S. Army.</p>
    </section>
    <div class="code-box"></div>

    <div class="spine">
      <span class="spine-title">IFR STUDY GUIDE</span>
      <span class="spine-sub">CHECKRIDE PREPARATION FOR <b>AIRPLANE</b> AND <b>HELICOPTER PILOTS</b></span>
      <span class="spine-author">MARCUS J. HOLLOWAY</span>
    </div>

    <section class="front">
      <h1 class="title">IFR STUDY GUIDE</h1>
      <p class="front-sub">CHECKRIDE PREPARATION FOR<br><b>AIRPLANE</b> AND <b>HELICOPTER PILOTS</b></p>
      <div class="front-tagline">PREPARE FOR YOUR INSTRUMENT RATING WITH CONFIDENCE</div>
      <div class="photo airliner" role="img" aria-label="Airliner flight deck with glass cockpit displays"></div>
      <div class="photo rotorcraft" role="img" aria-label="Helicopter instrument panel seen from the pilot seat"></div>
      <div class="front-author">MARCUS J. HOLLOWAY</div>
    </section>
  </div>
</div>
</body>
</html>
```